Poster Design for kebab shop products

need a new poster for our new velmo pack special, sign will be inside of shopping centre at different location to shop will need to stand out and draw customers to the store, MUST contain shops logo & picture added, poster size will be 76cm x 101cm so will need to suit that size

MUST ALSO CONTAIN THE FOLLOWING
Velmo Pack / HSP
Lamb & Chips
Chicken & Chips
Beef & Chips
+ Can $15

Target Market(s)

new customers

Industry/Entity Type

Retail

Font styles to use
Sans Serif

Colors

Designer to choose colors to be used in the design.

Requirements
Must have
• company logo
• picture of vemo pack provided
• Velmo Pack / HSP
• Lamb & Chips
• Chicken & Chips
• Beef & Chips
• + Can $15

```html
<!DOCTYPE html>
<html lang="en">
<head>
<meta charset="utf-8">
<title>Kebab Haven – Velmo Pack Special</title>
<link rel="stylesheet" href="https://fonts.googleapis.com/css2?family=Damion&family=Open+Sans:ital,wght@0,700;1,600&family=Yellowtail&display=block">
<style>
  :root {
    --sun-core: #f7e01a;
    --sun-mid: #f4c21f;
    --sun-edge: #ee8532;
    --brand-red: #b91f2b;
    --paper: #ffffff;
    --panel: #000000;
    --food-warm: #c99a4a;
    --food-light: #eef0f2;
  }
  html, body {
    margin: 0;
    padding: 0;
    width: 903px;
    height: 1200px;
    overflow: hidden;
    background: var(--sun-edge);
  }
  .poster {
    position: relative;
    width: 903px;
    height: 1200px;
    overflow: hidden;
    background: radial-gradient(ellipse 70% 60% at 50% 48%, var(--sun-core) 0%, var(--sun-mid) 55%, var(--sun-edge) 100%);
  }
  .brand-banner {
    position: absolute;
    left: 0;
    top: 0;
    width: 903px;
    height: 210px;
  }
  .brand-mark {
    position: absolute;
    left: 312px;
    top: 58px;
    width: 312px;
    display: flex;
    align-items: center;
    justify-content: center;
    gap: 10px;
    font-family: "Open Sans", sans-serif;
    font-weight: 700;
    font-size: 27px;
    color: var(--brand-red);
  }
  .brand-mark .dot {
    width: 22px;
    height: 22px;
    border-radius: 50%;
    background: var(--brand-red);
  }
  .hero-disc {
    position: absolute;
    left: 148px;
    top: 254px;
    width: 620px;
    height: 620px;
    border-radius: 50%;
    background: var(--paper);
    box-shadow: 0 10px 18px rgba(120, 60, 10, 0.35);
  }
  .headline {
    position: absolute;
    left: 56px;
    top: 248px;
    width: 790px;
    margin: 0;
    text-align: center;
    font-family: "Yellowtail", "Damion", cursive;
    font-weight: 400;
    font-size: 150px;
    line-height: 1.2;
    color: var(--brand-red);
    text-shadow: 4px 5px 0 var(--paper);
    white-space: nowrap;
  }
  .product-photo {
    position: absolute;
    left: 304px;
    top: 478px;
    width: 312px;
    height: 326px;
    border-radius: 18px;
    background: linear-gradient(180deg, var(--food-light) 0%, var(--food-light) 42%, var(--food-warm) 62%, #a06c3a 80%, var(--food-light) 100%);
  }
  .menu-panel {
    position: absolute;
    left: 44px;
    top: 940px;
    width: 822px;
    height: 234px;
    background: var(--panel);
    border-radius: 4px;
  }
  .menu-item {
    position: absolute;
    margin: 0;
    font-family: "Open Sans", sans-serif;
    font-style: italic;
    font-weight: 600;
    font-size: 38px;
    line-height: 1;
    color: var(--paper);
    white-space: nowrap;
  }
  .item-1 { left: 30px; top: 33px; }
  .item-2 { left: 30px; top: 101px; }
  .item-3 { left: 30px; top: 169px; }
  .item-4 { left: 512px; top: 33px; }
  .item-5 { left: 512px; top: 83px; }
</style>
</head>
<body>
<main class="poster">
  <svg class="brand-banner" viewBox="0 0 903 210" aria-hidden="true">
    <polygon points="314,-4 622,-4 622,198 460,152 314,202" fill="#ffffff" stroke="#b91f2b" stroke-width="5"/>
  </svg>
  <div class="brand-mark"><span class="dot"></span><span>Kebab Haven</span></div>

  <div class="hero-disc"></div>
  <h1 class="headline">Kebab Haven</h1>
  <div class="product-photo" role="img" aria-label="Photo of a Velmo Pack: chips topped with kebab meat, garlic and chilli sauce in an open foam takeaway box"></div>

  <section class="menu-panel">
    <p class="menu-item item-1">- Velmo Pack/ HSP</p>
    <p class="menu-item item-2">- Lamb &amp; Chips</p>
    <p class="menu-item item-3">- Chicken &amp; Chips</p>
    <p class="menu-item item-4">- Beef &amp; Chips</p>
    <p class="menu-item item-5">- + Can $15</p>
  </section>
</main>
</body>
</html>
```